Foot and ankle surgeon requires a website design

I need a website where prospective and established patients can obtain information and then direct them to making appointments. My practice is a highly professional surgical practice specialising in surgery to the foot and ankle. My title is Mr Colin Dwyer, Podiatric Foot & Ankle Surgeon. My qualifications are: BSc MSc FACPS
The practice website will require information on: Locations, phone numbers to make appointments, general background on podiatric surgery,
I would like to include information on: my hospital appointments, surgical fellowships held, training programs undertaken, association memberships, publications written, links to useful websites
A page dedicated to common foot conditions would be useful and also a page with referral information including an online registration section that will be sent direct to the receptionist.
Examples of similar websites include:
http://www.trevorkeplinfeet.com.au/
http://www.vollardfootsurgeon.com.au/
I will provide files on logo, self photos and my personal training history etc.
Also if there is going to be a background theme I personally am associated with surfing and beach activities, it would be great if this was able to be reflected in the design.
Thank you.

```html
<!DOCTYPE html>
<html lang="en">
<head>
<meta charset="utf-8">
<title>Mr Colin Dwyer – Podiatric Foot &amp; Ankle Surgeon</title>
<link href="https://fonts.googleapis.com/css2?family=Ubuntu:wght@400;500;700&display=swap" rel="stylesheet">
<style>
:root{
  --dark:#231f20;
  --blue:#0e4d85;
  --navy:#0f3f6e;
  --orange:#f7941d;
  --grey-text:#6b6b6b;
  --panel:#efefef;
  --tile:#ececec;
  --white:#ffffff;
}
*{margin:0;padding:0;box-sizing:border-box}
html,body{width:870px;height:1200px;overflow:hidden;background:var(--white)}
body{position:relative;font-family:'Ubuntu',sans-serif;color:var(--grey-text)}
.abs{position:absolute}

.topbar{left:0;top:0;width:870px;height:37px;background:var(--dark);color:var(--white);font-size:12px;display:flex;align-items:center;padding-left:96px;gap:14px}
.topbar .loc{display:flex;align-items:center;gap:6px}
.topbar svg{width:13px;height:15px}

.brand{left:96px;top:75px;display:flex;align-items:center;gap:8px}
.brand-mark{width:34px;height:34px;border-radius:50%;border:3px solid var(--orange)}
.brand-name{font-size:16px;font-weight:500;color:var(--navy)}

.search{left:593px;top:70px;width:181px;height:35px;background:var(--orange);padding:5px;display:flex;align-items:center}
.search-field{flex:1;height:25px;background:var(--white);font-size:12px;color:#333;display:flex;align-items:center;padding-left:12px}
.search-btn{width:28px;display:flex;justify-content:center}

.nav{left:0;top:136px;width:870px;height:58px;background:var(--blue)}
.nav ul{list-style:none;display:flex;position:absolute;left:95px;top:20px;gap:16px;font-size:12.3px;color:var(--white)}
.nav li.active{color:var(--orange)}

.hero{left:94px;top:194px;width:680px;height:275px;background:linear-gradient(180deg,#bfe3f6 0%,#8fd0ef 40%,#2fa9d8 60%,#7fcde6 78%,#e9eef0 100%)}
.hero h1{position:absolute;left:21px;top:28px;width:440px;font-size:29px;line-height:32px;font-weight:500;color:var(--navy)}
.dots{position:absolute;left:308px;top:249px;display:flex;gap:7px}
.dots span{width:11px;height:11px;border-radius:50%;background:var(--orange);border:2px solid var(--white)}
.dots span.on{background:var(--navy)}

.welcome{left:94px;top:482px;width:680px;text-align:center}
.section-title{font-size:24px;font-weight:400;color:var(--navy)}
.section-title em{font-style:normal;color:var(--orange)}
.welcome p{margin-top:8px;font-size:11.6px;line-height:17.6px}

.specialist{left:94px;top:590px;width:680px;height:207px;background:var(--panel)}
.specialist .section-title{position:absolute;top:18px;width:100%;text-align:center}
.specialist-photo{position:absolute;left:34px;top:66px;width:177px;height:106px;border:3px solid var(--white);background:linear-gradient(135deg,#5f8a6a,#d9b59c 55%,#f1e6de)}
.specialist p{position:absolute;left:236px;top:62px;width:412px;font-size:11.6px;line-height:17.6px}
.btn-appoint{position:absolute;left:236px;top:124px;width:227px;height:47px;background:var(--orange);color:var(--white);font-size:15px;font-weight:500;display:flex;align-items:center;justify-content:center;gap:10px}

.conditions{left:94px;top:814px;width:680px;text-align:center}
.conditions p{margin-top:10px;font-size:11.6px;line-height:17.6px;padding:0 14px}
.slider-arrows{left:728px;top:821px;display:flex;gap:6px}
.slider-arrows span{width:19px;height:18px;border:1px solid #d6d6d6;display:flex;align-items:center;justify-content:center}

.tile{width:146px;height:35px;background:var(--tile);display:flex;align-items:center;justify-content:space-between;padding:0 10px 0 12px;font-size:12px;color:var(--navy)}

.footer{left:0;top:1019px;width:870px;height:181px;background:var(--dark);color:var(--white)}
.footer-brand{position:absolute;left:96px;top:58px;display:flex;align-items:center;gap:8px;opacity:.35}
.footer-brand .brand-mark{border-color:#aaa}
.footer-brand .brand-name{color:#bbb}
.social{position:absolute;left:96px;top:139px;display:flex;gap:9px}
.social span{width:20px;height:20px;border-radius:50%;border:1.5px solid var(--white)}
.footer h3{position:absolute;font-size:19px;font-weight:500;color:var(--orange)}
.contact-col{position:absolute;top:51px;width:150px;font-size:11.5px;line-height:20.5px;white-space:nowrap}
.contact-col strong{display:block;font-weight:700;margin-bottom:6px}
.contact-col b{font-weight:400;color:var(--orange)}
.hours{position:absolute;left:626px;top:47px;font-size:12px;line-height:20.5px}
.copyright{position:absolute;left:635px;top:117px;font-size:9.5px}
</style>
</head>
<body>

<div class="abs topbar">
  <span>Our Locations :</span>
  <span class="loc"><svg viewBox="0 0 13 15"><path d="M6.5 1a4.5 4.5 0 0 0-4.5 4.5C2 9 6.5 14 6.5 14S11 9 11 5.5A4.5 4.5 0 0 0 6.5 1z" fill="none" stroke="#fff" stroke-width="1.4"/><circle cx="6.5" cy="5.5" r="1.6" fill="#fff"/></svg>Westhaven &nbsp;Ph: 08-9100-2741</span>
  <span class="loc"><svg viewBox="0 0 13 15"><path d="M6.5 1a4.5 4.5 0 0 0-4.5 4.5C2 9 6.5 14 6.5 14S11 9 11 5.5A4.5 4.5 0 0 0 6.5 1z" fill="none" stroke="#fff" stroke-width="1.4"/><circle cx="6.5" cy="5.5" r="1.6" fill="#fff"/></svg>Goldridge &nbsp;ph: 08-9100-5826</span>
</div>

<div class="abs brand">
  <span class="brand-mark"></span>
  <span class="brand-name">Mr Colin Dwyer</span>
</div>

<div class="abs search">
  <div class="search-field">Search here...</div>
  <div class="search-btn"><svg width="13" height="13" viewBox="0 0 13 13"><circle cx="5.5" cy="5.5" r="4" fill="none" stroke="#fff" stroke-width="2"/><path d="M8.5 8.5l3.5 3.5" stroke="#fff" stroke-width="2"/></svg></div>
</div>

<nav class="abs nav">
  <ul>
    <li class="active">Home</li><li>Appointments</li><li>surgical fellowships</li><li>trainingprograms</li><li>memberships</li><li>publications</li><li>useful websites</li><li>contact us</li>
  </ul>
</nav>

<section class="abs hero" role="img" aria-label="Photo of bare feet crossed against a sunny beach and turquoise sea">
  <h1>Working hard to keep you on your feet</h1>
  <div class="dots"><span class="on"></span><span></span><span></span><span></span></div>
</section>

<section class="abs welcome">
  <h2 class="section-title">Welcome to <em>Colin Dwyer</em></h2>
  <p>For those unfamiliar with our services, we are a team of accredited health professionals dealing with the prevention, diagnosis, treatment and rehabilitation of medical and surgical conditions related to feet, ankles and lower limbs.Many foot and lower limb problems, if identified early can be prevented, so take the right step and contact the Coastline Foot Care Group.</p>
</section>

<section class="abs specialist">
  <h2 class="section-title">Specialist <em>Podiatric</em> Surgeon</h2>
  <div class="specialist-photo" role="img" aria-label="Photo of a clinician testing a patient's foot reflex"></div>
  <p>Lorem ipsum dolor sit amet, ut his facete constituam definitiones. Duo dictas facilis accusamus at, qui ei nihil vivendum. His numquam laoreet te. At legimus postulant repudiandae est, idque choro at quo. Veritus luptatum detraxit cu.</p>
  <div class="btn-appoint"><svg width="18" height="18" viewBox="0 0 18 18"><circle cx="9" cy="9" r="9" fill="#fff"/><path d="M5 9h7M9 5.5L12.5 9 9 12.5" fill="none" stroke="#f7941d" stroke-width="2"/></svg>Make an Appointment</div>
</section>

<section class="abs conditions">
  <h2 class="section-title">Foot Conditions</h2>
  <p>Lus quas perpetua eu, ut vim percipit qualisque concludaturque. In soleat eloquentiam eam, his ad numquam voluptua. Has sumo perpetua no. Cu vis justo tollit.</p>
</section>
<div class="abs slider-arrows">
  <span><svg width="7" height="10" viewBox="0 0 7 10"><path d="M6 1L2 5l4 4" fill="none" stroke="#0f3f6e" stroke-width="1.6"/></svg></span>
  <span><svg width="7" height="10" viewBox="0 0 7 10"><path d="M1 1l4 4-4 4" fill="none" stroke="#0f3f6e" stroke-width="1.6"/></svg></span>
</div>

<div class="abs tile" style="left:112px;top:904px">Ankle Sprains<svg width="12" height="10" viewBox="0 0 12 10"><path d="M0 5h7M6 1l5 4-5 4z" fill="#999" stroke="#999" stroke-width="2"/></svg></div>
<div class="abs tile" style="left:276px;top:904px">Hallux Rigidus<svg width="12" height="10" viewBox="0 0 12 10"><path d="M0 5h7M6 1l5 4-5 4z" fill="#999" stroke="#999" stroke-width="2"/></svg></div>
<div class="abs tile" style="left:440px;top:904px">Hallux Valgus<svg width="12" height="10" viewBox="0 0 12 10"><path d="M0 5h7M6 1l5 4-5 4z" fill="#999" stroke="#999" stroke-width="2"/></svg></div>
<div class="abs tile" style="left:604px;top:904px">Hallux Valgus<svg width="12" height="10" viewBox="0 0 12 10"><path d="M0 5h7M6 1l5 4-5 4z" fill="#999" stroke="#999" stroke-width="2"/></svg></div>
<div class="abs tile" style="left:112px;top:954px">Hammer Toes<svg width="12" height="10" viewBox="0 0 12 10"><path d="M0 5h7M6 1l5 4-5 4z" fill="#999" stroke="#999" stroke-width="2"/></svg></div>
<div class="abs tile" style="left:276px;top:954px">Morton's Neuroma<svg width="12" height="10" viewBox="0 0 12 10"><path d="M0 5h7M6 1l5 4-5 4z" fill="#999" stroke="#999" stroke-width="2"/></svg></div>
<div class="abs tile" style="left:440px;top:954px">Severs Disease<svg width="12" height="10" viewBox="0 0 12 10"><path d="M0 5h7M6 1l5 4-5 4z" fill="#999" stroke="#999" stroke-width="2"/></svg></div>
<div class="abs tile" style="left:604px;top:954px">Hallux Valgus<svg width="12" height="10" viewBox="0 0 12 10"><path d="M0 5h7M6 1l5 4-5 4z" fill="#999" stroke="#999" stroke-width="2"/></svg></div>

<footer class="abs footer">
  <div class="footer-brand"><span class="brand-mark"></span><span class="brand-name">Mr Colin Dwyer</span></div>
  <div class="social"><span></span><span></span><span></span></div>

  <h3 style="left:295px;top:18px">Contact Details</h3>
  <div class="contact-col" style="left:295px">
    <strong>Westhaven</strong>
    <b>P :</b> 08-9100-2741<br><b>F :</b> 08-9100-2795<br><b>M :</b> info@cdfoot.com.au
  </div>
  <div class="contact-col" style="left:457px">
    <strong>Goldridge</strong>
    <b>P :</b> 08-9100-5826<br><b>F :</b> 08-9100-5860<br><b>M :</b> info@cdfoot.com.au
  </div>

  <h3 style="left:626px;top:18px">Office Hours</h3>
  <div class="hours">Mon - Fri: 9:00am - 5:00pm<br>Sat: 9:00am - 2:00pm</div>
  <div class="copyright">© Copyright 2014 Colin Dwyer.</div>
</footer>

</body>
</html>
```